Medien Firma benötigt Briefpapier
Zielgruppe
Firma:
Wir sind im Bereich Veranstaltungstechnik und Eventmanagement seit 2007 tätig. Ab 2009 konnten wir unsere Expertise um die Bereiche Medientechnik und TV Produktion erweitern. Durch dieses Portfolio sind wir in der Lage, alle Facetten der technischen Planung durchzuführen.
Bereiche:
Veranstaltungstechnik - Medientechnik - Livestreaming
Kunden:
B2B
Aufgabenstellung
Erstellung von Briefpapier mit dem vorhandenen Logo.
Das Briefpapier soll auch als Produktsheet nutzbar sein. Also muss der Footer Text austauschbar sein.
Schlicht, Modern, Zeitlos, max. zwei Farben

```html
<!DOCTYPE html>
<html lang="de">
<head>
<meta charset="utf-8">
<title>Velmora Events – Briefpapier</title>
<link rel="stylesheet" href="https://fonts.googleapis.com/css2?family=Open+Sans:wght@400;600;700&display=swap">
<style>
  :root {
    --stage: #95a3a9;
    --paper: #ffffff;
    --brand-blue: #009ade;
    --tint-blue: #e0f3fa;
    --ink: #1c1c1c;
    --page-w: 400px;
    --page-h: 566px;
  }
  * { margin: 0; padding: 0; box-sizing: border-box; }
  html, body {
    width: 1200px;
    height: 971px;
    overflow: hidden;
  }
  body {
    background: var(--stage);
    font-family: "Open Sans", Arial, sans-serif;
    color: var(--ink);
    position: relative;
  }
  .sheet {
    position: absolute;
    top: 202px;
    width: var(--page-w);
    height: var(--page-h);
    background: var(--paper);
    overflow: hidden;
  }
  .sheet--letterhead { left: 150px; }
  .sheet--cover { left: 650px; background: var(--brand-blue); }

  .sheet__shape {
    position: absolute;
    inset: 0;
    width: 100%;
    height: 100%;
  }
  .shape--tint { fill: var(--tint-blue); }
  .shape--white { fill: var(--paper); }

  .company-name {
    position: absolute;
    font-weight: 600;
    color: var(--ink);
    white-space: nowrap;
    text-transform: uppercase;
    letter-spacing: 0.14em;
  }
  .sheet--letterhead .company-name {
    right: 40px;
    top: 70px;
    font-size: 13px;
  }
  .sheet--cover .company-name {
    left: 32px;
    top: 262px;
    font-size: 21px;
  }

  .sender {
    position: absolute;
    left: 44px;
    top: 76px;
    font-size: 4.6px;
    line-height: 1.4;
  }
  .sender__name { color: var(--brand-blue); font-weight: 700; }

  .footer {
    position: absolute;
    left: 44px;
    right: 44px;
    bottom: 34px;
    font-size: 4.6px;
    line-height: 1.6;
  }
  .footer__rule {
    height: 0.8px;
    background: var(--brand-blue);
    opacity: 0.6;
    margin-bottom: 5px;
  }
  .footer__link { color: var(--brand-blue); font-weight: 700; }
</style>
</head>
<body>

  <section class="sheet sheet--letterhead" aria-label="Briefbogen">
    <svg class="sheet__shape" viewBox="0 0 100 100" preserveAspectRatio="none" aria-hidden="true">
      <polygon class="shape--tint" points="0,0 87,50 0,100"/>
    </svg>

    <div class="sender">
      <p class="sender__name">Velmora Events</p>
      <p>Musterstraße 1 | 12345 Musterstadt | info@velmora-events.de</p>
    </div>

    <p class="company-name">Velmora Events</p>

    <footer class="footer">
      <div class="footer__rule"></div>
      <p>Musterstraße 1 | 12345 Musterstadt | Tel. 0123 456 789 | info@velmora-events.de | <span class="footer__link">www.velmora-events.de</span></p>
      <p>Finanzamt Musterstadt | USt-ID DE 123 456 789 | BV Musterbank | BIC ABCDEFGH | IBAN DE 1234 5678 9012 3456 7890</p>
    </footer>
  </section>

  <section class="sheet sheet--cover" aria-label="Produktblatt Rückseite">
    <svg class="sheet__shape" viewBox="0 0 100 100" preserveAspectRatio="none" aria-hidden="true">
      <polygon class="shape--white" points="0,0 89,51 0,100"/>
    </svg>

    <p class="company-name">Velmora Events</p>
  </section>

</body>
</html>
```